Business cards for a tribute and obituary website

Our website is called Quiet Orchard.

It is a special place online for people to remember their loved ones who have passed away, through obituaries and tributes. Friends and family can also convey their condolences on the deceased's memorial page. Celebrating the life of the deceased and remembering their legacy is very important to us – death should not be just about grieving.

We would like the card to look tasteful and modern. The design should ideally not have colours that are too bright. The logo and website URL, www.quietorchardpages.net should be visible on the front of the card, with our slogan "Celebrating a life passed" on the back.

The design should communicate our purpose – remembering loved ones who have passed – and also a lighter tone of celebrating life. It should not look like a funeral director's card!

Our logo has been attached. Looking forward to some beautiful designs! Get creative :)
Updates

Reason: Thank you all for your designs. The rest of my team and I have not reached a decision on which design to select and I am collecting feedback from them. I will provide feedback for any changes that need to be made soon. It would be great if we could see more original designs and in more colours! We will definitely select a design by this deadline.

Industry/Entity Type

Business

Contact Information for Business Card

Nadia Fenwick
Project Manager
471226809
nadiafenwick@quietorchardpages.net

Font styles to use
Serif
Sans Serif

Requirements
Must have
• Logo and website address (www.quietorchardpages.net) on the front.
Nice to have
• Hi designers! It would be nice to see alternative colours – feel free to try out colours that are tasteful and subtle. The colour of the business card does not have to be the same as the logo.
• We would also like to see the logo used in different ways, perhaps a glossy or embossed finish. The card should look stylish.

```html
<!DOCTYPE html>
<html lang="en">
<head>
<meta charset="utf-8">
<title>Quiet Orchard – Business Cards</title>
<link rel="stylesheet" href="https://fonts.googleapis.com/css2?family=Lato:wght@400;700&display=swap">
<style>
  :root {
    --backdrop: #1f1f21;
    --navy: #0f3357;
    --navy-deep: #0b2946;
    --paper: #f4f4f4;
    --paper-shade: #e4e4e4;
    --ink: #3a3a3a;
    --ink-navy: #1d3f66;
    --muted-navy: #5a7090;
    --white: #ffffff;
    --slogan: #dfe5ec;
  }
  * { box-sizing: border-box; margin: 0; padding: 0; }
  html, body {
    width: 1200px; height: 873px; overflow: hidden;
    background: var(--backdrop);
    font-family: "Lato", sans-serif;
  }
  .stage {
    width: 1200px; height: 873px;
    display: flex; align-items: center; justify-content: center; gap: 40px;
  }
  .card {
    width: 540px; height: 309px; position: relative; overflow: hidden;
  }

  /* Front */
  .card-front { background: var(--paper); display: flex; flex-direction: column; }
  .front-header {
    height: 96px; background: var(--navy);
    display: flex; align-items: center; justify-content: center; gap: 14px;
  }
  .brand-dot { width: 26px; height: 26px; border-radius: 50%; background: var(--white); flex: none; }
  .brand-name {
    color: var(--white); font-weight: 700; font-size: 30px; letter-spacing: 0.5px; white-space: nowrap;
  }
  .front-body {
    flex: 1; background: linear-gradient(180deg, var(--paper) 0%, var(--paper-shade) 100%);
    position: relative;
  }
  .contact-list {
    position: absolute; top: 26px; right: 28px; list-style: none;
    font-size: 12.5px; color: var(--ink); white-space: nowrap;
  }
  .contact-list li { display: flex; align-items: center; gap: 10px; margin-bottom: 9px; }
  .contact-list svg { width: 13px; height: 13px; flex: none; fill: none; stroke: var(--ink-navy); stroke-width: 1.6; }
  .person { position: absolute; left: 32px; bottom: 28px; }
  .person-name { font-weight: 700; font-size: 19px; color: var(--ink-navy); }
  .person-role { font-size: 14px; color: var(--muted-navy); margin-top: 2px; }
  .person-address { font-weight: 700; font-size: 13px; color: var(--ink); margin-top: 14px; }
  .front-footer { height: 14px; background: var(--navy); }

  /* Back */
  .card-back {
    background: radial-gradient(circle at 50% 40%, var(--navy) 0%, var(--navy-deep) 100%);
    display: flex; flex-direction: column; align-items: center; justify-content: center;
  }
  .back-brand { display: flex; align-items: center; gap: 16px; margin-top: -10px; }
  .back-brand .brand-dot { width: 40px; height: 40px; }
  .back-brand .brand-name { font-size: 38px; }
  .slogan {
    position: absolute; bottom: 34px; left: 0; right: 0; text-align: center;
    color: var(--slogan); font-weight: 700; font-size: 15px; letter-spacing: 4px; text-transform: uppercase;
  }
</style>
</head>
<body>
<main class="stage">
  <section class="card card-front">
    <header class="front-header">
      <span class="brand-dot"></span>
      <span class="brand-name">Quiet Orchard</span>
    </header>
    <div class="front-body">
      <ul class="contact-list">
        <li>
          <svg viewBox="0 0 14 14"><path d="M3 1.5h2l1 3-1.5 1a7 7 0 0 0 4 4l1-1.5 3 1v2c0 .8-.7 1.5-1.5 1.5A11 11 0 0 1 1.5 3c0-.8.7-1.5 1.5-1.5z"/></svg>
          471226809
        </li>
        <li>
          <svg viewBox="0 0 14 14"><rect x="1" y="3" width="12" height="8"/><path d="M1 3l6 5 6-5"/></svg>
          nadiafenwick@quietorchardpages.net
        </li>
        <li>
          <svg viewBox="0 0 14 14"><rect x="1.5" y="5" width="6" height="4" rx="2" transform="rotate(-45 4.5 7)"/><rect x="6.5" y="5" width="6" height="4" rx="2" transform="rotate(-45 9.5 7)"/></svg>
          www.quietorchardpages.net
        </li>
      </ul>
      <div class="person">
        <p class="person-name">Nadia Fenwick</p>
        <p class="person-role">Project Manager</p>
        <p class="person-address">52 Linden Row, Fairhollow, PA 15990</p>
      </div>
    </div>
    <footer class="front-footer"></footer>
  </section>

  <section class="card card-back">
    <div class="back-brand">
      <span class="brand-dot"></span>
      <span class="brand-name">Quiet Orchard</span>
    </div>
    <p class="slogan">Celebrating a life passed</p>
  </section>
</main>
</body>
</html>
```